AI Business Tools Landing Page

My web-based website builder (Nurvanta.com) will be adding many new features in the very near future and I need an eye-catching landing page to promote these new products.

The page will have a primary section of the 8 main products we are promoting:
1. AI Instant Website Generator
2. AI Chatbot
3. Online Store Builder with AI Assistance
4. AI Auto-Blogging System
5. Online Scheduling System
6. Custom Email System
7. SEO Service
8. CRM System

The page will also have a smaller section for links to our affiliate programs. These can be smaller, less-promanent buttons or links. These are the affiliate products:
1. Get Your LLC
2. Website Design and Maintenance
3. Tavolin Ads Management
4. Social Media Posting Service
5. Logo Design
6. Trademark Registration
7. Patent Application
8. Printing Services (including postcards, flyers, and merch.)
9. Bulk AI Content Generator

The theme and color scheme of the page should follow the theme of our main website, which is https://nurvanta.com.

I need the page fully coded and ready to deploy on my server.

I look forward to seeing your amazing designs!

```html
<!DOCTYPE html>
<html lang="en">
<head>
<meta charset="UTF-8">
<title>Nurvanta – AI Business Tools</title>
<link href="https://fonts.googleapis.com/css2?family=Lexend:wght@500;600;700&family=Poppins:wght@400;500;600&display=swap" rel="stylesheet">
<style>
:root{
  --navy:#0d1a3a;
  --navy-deep:#0a1836;
  --blue:#2f8be6;
  --sky:#3cb4f7;
  --sky-soft:#e6f3fd;
  --green:#7fd9a8;
  --text:#3e4860;
  --white:#ffffff;
}
*{margin:0;padding:0;box-sizing:border-box}
html,body{width:1200px;height:4501px;overflow:hidden}
body{position:relative;background:var(--white);font-family:"Poppins",sans-serif;color:var(--navy)}
.abs{position:absolute}
.brand{display:flex;align-items:center;gap:14px;font-family:"Lexend",sans-serif;font-weight:600;font-size:36px;color:var(--navy)}
.brand-dot{width:52px;height:52px;border-radius:50%;background:var(--sky)}
.btn{display:inline-flex;align-items:center;justify-content:center;background:var(--green);color:var(--white);font-family:"Poppins",sans-serif;font-weight:600;font-size:12px;border-radius:20px;text-decoration:none}
.hero-bg{left:0;top:0;width:1200px;height:560px}
.art{border-radius:24px}
.title{font-family:"Lexend",sans-serif;font-weight:600;font-size:40px;line-height:51px;color:var(--navy)}
.hl{background:linear-gradient(to bottom,transparent 45%,var(--sky) 45%,var(--sky) 92%,transparent 92%);padding:0 2px}
.body{position:absolute;border-left:1.5px solid var(--blue);padding-left:56px;padding-top:34px}
.body::after{content:"";position:absolute;left:-6px;bottom:-2px;width:8px;height:8px;border-right:1.5px solid var(--blue);border-bottom:1.5px solid var(--blue);transform:rotate(45deg)}
.body::before{content:"";position:absolute;left:0;top:0;width:var(--reach,200px);border-top:1.5px solid var(--blue)}
.tick{list-style:none}
.tick li{position:relative;padding-left:18px;font-size:11.5px;line-height:19px;color:var(--text);margin-bottom:18px}
.tick li::before{content:"";position:absolute;left:0;top:5px;width:9px;height:5px;border-left:2px solid var(--sky);border-bottom:2px solid var(--sky);transform:rotate(-45deg)}
.resources-bg{left:0;top:3440px;width:1200px;height:760px}
.frame{left:105px;top:3695px;width:990px;height:297px;border:1.5px solid var(--blue)}
.res-title{left:0;top:3703px;width:1200px;text-align:center;font-family:"Lexend",sans-serif;font-weight:500;font-size:37px;line-height:44px;color:var(--navy)}
.chip-row{left:0;width:1200px;display:flex;justify-content:center;gap:12px}
.chip{height:36px;padding:0 24px;display:flex;align-items:center;border:1.5px solid #9cc7f0;background:var(--white);color:var(--blue);font-size:12px;font-weight:600}
.chip.active{background:var(--sky);color:var(--white);border-color:var(--sky)}
.footer-bg{left:0;top:4100px;width:1200px;height:401px}
.footer-text{left:0;top:4300px;width:1200px;text-align:center;color:var(--white);font-size:13px;line-height:20px}
.socials{left:0;top:4371px;width:1200px;display:flex;justify-content:center;gap:8px}
.socials span{width:20px;height:20px;border-radius:50%;border:1px solid #3b6fc8}
.socials span.on{background:var(--blue)}
.copy{left:0;top:4430px;width:1200px;text-align:center;color:#c8d2e6;font-size:11px}
.copy b{color:var(--sky);font-weight:500}
</style>
</head>
<body>

<svg class="abs hero-bg" viewBox="0 0 1200 560" preserveAspectRatio="none" aria-hidden="true">
  <defs><linearGradient id="heroG" x1="0" y1="0" x2="0" y2="1"><stop offset="0" stop-color="#eef7fe"/><stop offset="1" stop-color="#d6ecfb"/></linearGradient></defs>
  <path d="M0 0H1200V440C1060 400 940 560 720 540C520 520 260 450 0 470Z" fill="url(#heroG)"/>
</svg>

<header>
  <div class="abs brand" style="left:106px;top:26px"><span class="brand-dot"></span>Nurvanta</div>
  <a class="abs btn" href="https://nurvanta.com" style="left:907px;top:30px;width:187px;height:35px">Get started for free!</a>
</header>

<section class="feature">
  <h1 class="abs title" style="left:108px;top:170px">AI Instant <span class="hl">Website</span><br><span class="hl">Generator</span></h1>
  <div class="body" style="left:152px;top:230px;height:175px;--reach:255px">
    <ul class="tick" style="margin-top:4px;width:330px">
      <li>Get a professional, seo-optimized website in seconds!</li>
      <li>Includes custom domain, secure high-speed hosting, professional images, and more!</li>
    </ul>
  </div>
  <div class="abs art" role="img" aria-label="Illustration of a robot building a website on a desktop monitor with plants and gears" style="left:629px;top:148px;width:466px;height:289px;background:linear-gradient(135deg,#8fa8f5,#5a7de6 60%,#f4b04d)"></div>
</section>

<section class="feature">
  <div class="abs art" role="img" aria-label="Illustration of a chatbot robot greeting a person from a phone screen" style="left:122px;top:620px;width:376px;height:288px;background:linear-gradient(135deg,#fde3d3,#7fb8f5)"></div>
  <h2 class="abs title" style="left:615px;top:648px">AI C<span class="hl">hatbot</span></h2>
  <div class="body" style="left:650px;top:708px;height:155px;--reach:185px">
    <ul class="tick" style="width:380px">
      <li>Fully-Trainable chatbot will learn about your business to automate the customer support process!</li>
      <li>Built-In crm features integrate emailing, text messaging, and contact forms!</li>
    </ul>
  </div>
</section>

<section class="feature">
  <h2 class="abs title" style="left:108px;top:1032px">Online Store Builder<br>(E-Commerce) <span class="hl">With AI</span><br><span class="hl">Assistance</span></h2>
  <div class="body" style="left:143px;top:1144px;height:170px;--reach:410px">
    <ul class="tick" style="width:380px">
      <li>Sell you products online and integrate your products into any website!</li>
      <li>Accept payments from multiple payment gateways including Strivo and Paylane!</li>
    </ul>
  </div>
  <div class="abs art" role="img" aria-label="Isometric illustration of people shopping online around a laptop with a robot assistant" style="left:699px;top:987px;width:393px;height:367px;background:linear-gradient(135deg,#eaf2fd,#6d8ef0 70%,#e04a4a)"></div>
</section>

<section class="feature">
  <div class="abs art" role="img" aria-label="Illustration of a laptop with blog articles and media floating above the screen" style="left:105px;top:1415px;width:393px;height:367px;background:linear-gradient(135deg,#b9a9ef,#7fe0d8 70%,#eef3fb)"></div>
  <h2 class="abs title" style="left:615px;top:1478px">AI Auto-<span class="hl">Blogging</span><br><span class="hl">System</span></h2>
  <div class="body" style="left:650px;top:1572px;height:150px;--reach:300px">
    <ul class="tick" style="width:390px">
      <li>AI will generate an incredible blog for your business in seconds and immediately begin posting content for you!</li>
      <li>Choose from daily, weekly, or monthly automated blog posting. consistent, unique, seo-optimized content posting on cruise control!</li>
    </ul>
  </div>
</section>

<section class="feature">
  <h2 class="abs title" style="left:108px;top:1864px">Online <span class="hl">Scheduling</span><br><span class="hl">System</span></h2>
  <div class="body" style="left:143px;top:1960px;height:145px;--reach:210px">
    <ul class="tick" style="width:400px">
      <li>Get Appointment Bookings, Restaurant Reservations, Or Consultations Scheduled Directly From Your Website!</li>
      <li>Manage Your Employees' Schedules And All Your Appointments From A Simple, User-Friendly Dashboard!</li>
    </ul>
  </div>
  <div class="abs art" role="img" aria-label="Illustration of a person marking dates on a large calendar beside a clock" style="left:699px;top:1860px;width:393px;height:236px;background:linear-gradient(135deg,#e3efff,#6f95ee 65%,#f4a64a)"></div>
</section>

<section class="feature">
  <div class="abs art" role="img" aria-label="Illustration of a phone with an email envelope and people working around it" style="left:105px;top:2175px;width:393px;height:306px;background:linear-gradient(135deg,#dfe9fd,#7d97ee)"></div>
  <h2 class="abs title" style="left:613px;top:2210px">Custom Emails<br><span class="hl">Using Your Domain</span></h2>
  <div class="body" style="left:650px;top:2304px;height:150px;--reach:330px">
    <ul class="tick" style="width:395px">
      <li>Quickly set up emails for yourself and all your employees with your own domain extension (example - johnd@yoursite.com). no more unprofessional Mailora and Yondomail email addresses!</li>
      <li>Manage all your business emails from a simple, user-friendly interface!</li>
    </ul>
  </div>
</section>

<section class="feature">
  <h2 class="abs title" style="left:108px;top:2566px">SEO Service –<br>Automatic <span class="hl">Backlink</span><br><span class="hl">Building</span></h2>
  <div class="body" style="left:143px;top:2716px;height:205px;--reach:360px">
    <ul class="tick" style="width:380px">
      <li>Let us do the hard work of getting high-quality backlinks to your website. although difficult to get, backlinks to your website boost search engine ranking more than any other strategy!</li>
      <li>Subscribe now and start getting 10-20 high-quality permanent backlinks to your website every month, guaranteed!</li>
    </ul>
  </div>
  <div class="abs art" role="img" aria-label="Isometric illustration of large SEO letters surrounded by gears and a keyboard" style="left:699px;top:2559px;width:393px;height:350px;background:linear-gradient(135deg,#eef3fb,#3b57c9 60%,#9fb3f2)"></div>
</section>

<section class="feature">
  <div class="abs art" role="img" aria-label="Isometric illustration of CRM dashboard with charts and analytics panels" style="left:105px;top:2996px;width:393px;height:323px;background:linear-gradient(135deg,#cfe6ff,#6aa9f2 60%,#e9f1fd)"></div>
  <h2 class="abs title" style="left:615px;top:3054px">CRM <span class="hl">System</span></h2>
  <div class="body" style="left:650px;top:3113px;height:155px;--reach:210px">
    <ul class="tick" style="width:390px">
      <li>Automate the lead follow up process to consistently stay in front of your potential customers!</li>
      <li>Chedule automatic email and text campaigns and effortlessly follow your funnels from lead to closing!</li>
    </ul>
  </div>
  <a class="abs btn" href="https://nurvanta.com" style="left:507px;top:3354px;width:187px;height:35px">Get started for free!</a>
</section>

<section class="resources">
  <svg class="abs resources-bg" viewBox="0 0 1200 760" preserveAspectRatio="none" aria-hidden="true">
    <path d="M0 70C180 20 360 10 600 60C820 100 1000 80 1200 40V760H0Z" fill="#eef6fe"/>
  </svg>
  <span class="abs" style="left:557px;top:3548px;width:86px;height:86px;border-radius:50%;background:var(--sky)"></span>
  <div class="abs frame"></div>
  <h2 class="abs res-title"><span style="background:#eef6fe;padding:0 30px">Additional resources to help launch</span><br>your business</h2>
  <div class="abs chip-row" style="top:3825px">
    <a class="chip">Get Your LLC</a>
    <a class="chip active">Website Design And Maintenance</a>
    <a class="chip">Tavolin Ads Management</a>
    <a class="chip">Social Media Posting Service</a>
  </div>
  <div class="abs chip-row" style="top:3876px">
    <a class="chip">Logo Design</a>
    <a class="chip">Trademark Registration</a>
    <a class="chip">Patent Application</a>
    <a class="chip">Printing Services</a>
    <a class="chip">Bulk AI Content Generator</a>
  </div>
  <a class="abs btn" href="https://nurvanta.com" style="left:489px;top:3975px;width:222px;height:35px">Explore Our Affiliate Programs</a>
</section>

<footer>
  <svg class="abs footer-bg" viewBox="0 0 1200 401" preserveAspectRatio="none" aria-hidden="true">
    <path d="M0 50C200 0 420 10 640 30C860 50 1040 10 1200 30V401H0Z" fill="var(--navy-deep)"/>
  </svg>
  <div class="abs brand" style="left:0;top:4200px;width:1200px;justify-content:center;color:var(--white)"><span class="brand-dot"></span>Nurvanta</div>
  <p class="abs footer-text">It'll take minutes or less! just answer a few basic questions and watch your<br>stunning new website generate in seconds!</p>
  <div class="abs socials"><span></span><span></span><span class="on"></span><span></span><span></span><span></span><span></span><span></span><span></span><span></span></div>
  <p class="abs copy">© 2024 <b>Nurvanta</b>. All Rights Reserved</p>
</footer>

</body>
</html>
```